Emotional Historical Fiction Book Cover Design

The novel is about the Chernobyl incident. I interviewed several people with first-hand accounts, and it's an emotional event. I'd like to have it published, but will need a cover for it.

The story follows the path of 3 characters, a child, a young woman and an elderly man. The theme of memory and nostalgia flow through each, as well as the feeling of being uprooted.

The title is "the hum of kettles" and is metaphorical to the story. I imagine the design will be as simplistic as possible.

Target Market(s)

teen - adult; 18+

Industry/Entity Type

Event

Colors

Designer to choose colors to be used in the design.

Requirements
Must have
• the title: the hum of kettles (in all lower case)
• the author: Brenna Holtzwinder
• Somewhere "a novel" must be written

```html
<!DOCTYPE html>
<html lang="en">
<head>
<meta charset="utf-8">
<title>the hum of kettles — Brenna Holtzwinder</title>
<link rel="stylesheet" href="https://fonts.googleapis.com/css2?family=Barlow+Condensed:wght@600;700&family=Barlow+Semi+Condensed:wght@700&display=swap">
<style>
  :root {
    --backdrop: #e4e4e4;
    --ink: #0b0b09;
    --light-yellow: #e9e3a6;
    --olive: #a49a52;
    --umber: #5a4a2a;
    --shadow-brown: #24190f;
  }
  * { margin: 0; padding: 0; box-sizing: border-box; }
  html, body {
    width: 1200px;
    height: 1200px;
    overflow: hidden;
    background: var(--backdrop);
  }
  .book-cover {
    position: absolute;
    left: 230px;
    top: 45px;
    width: 740px;
    height: 1110px;
    overflow: hidden;
    box-shadow: 0 6px 24px rgba(0, 0, 0, 0.18);
  }
  .cover-photo {
    position: absolute;
    inset: 0;
    width: 100%;
    height: 100%;
  }
  .author {
    position: absolute;
    top: 52px;
    left: 0;
    width: 100%;
    text-align: center;
    font-family: "Barlow Condensed", "Arial Narrow", sans-serif;
    font-weight: 700;
    font-size: 36px;
    letter-spacing: 0.5px;
    text-transform: uppercase;
    color: var(--ink);
  }
  .title {
    font-family: "Barlow Semi Condensed", "Arial Narrow", sans-serif;
    font-weight: 700;
    color: var(--ink);
    line-height: 0.8;
    letter-spacing: -3px;
  }
  .title-word {
    position: absolute;
    display: block;
  }
  .title-the { left: 250px; top: 350px; font-size: 160px; }
  .title-hum { left: 300px; top: 470px; font-size: 160px; }
  .title-of { left: 175px; top: 610px; font-size: 96px; letter-spacing: -2px; }
  .title-kettles { left: 230px; top: 670px; font-size: 168px; }
  .tagline {
    position: absolute;
    left: 300px;
    top: 850px;
    font-family: "Barlow Condensed", "Arial Narrow", sans-serif;
    font-weight: 600;
    font-size: 46px;
    text-transform: uppercase;
    color: var(--ink);
  }
</style>
</head>
<body>
  <main class="book-cover">
    <svg class="cover-photo" role="img" aria-label="Photograph of an abandoned, decaying school corridor with peeling walls, open windows and debris on the floor, in a faded yellow-brown tone" viewBox="0 0 740 1110" preserveAspectRatio="none">
      <defs>
        <radialGradient id="corridor-light" cx="0.55" cy="0.38" r="0.75">
          <stop offset="0" stop-color="var(--light-yellow)"/>
          <stop offset="0.35" stop-color="var(--olive)"/>
          <stop offset="0.75" stop-color="var(--umber)"/>
          <stop offset="1" stop-color="var(--shadow-brown)"/>
        </radialGradient>
      </defs>
      <rect width="740" height="1110" fill="url(#corridor-light)"/>
    </svg>

    <p class="author">Brenna Holtzwinder</p>

    <h1 class="title">
      <span class="title-word title-the">the</span>
      <span class="title-word title-hum">hum</span>
      <span class="title-word title-of">of</span>
      <span class="title-word title-kettles">kettles</span>
    </h1>

    <p class="tagline">A Novel</p>
  </main>
</body>
</html>
```